Journeys With Marcella Business Cards

I need a business card design for my upscale Travel Agency.
Attached you can find my logo.
I would like to include the following:
- Name
- Title
- Phone Number
- Email
- Website
- and then something like: Follow us: JourneysWithMarcella (and then social media icons in color).
The logo should be in the front and then also the back.
I am also attaching a design that I liked (mostly for the layout) but open to any suggestions
Industry/Entity Type
Travel Agent
Contact Information for Business Card
Name: Marcella Dorn
Title: Travel Designer / Owner
Phone: 415-927-3308
Email: marcella@journeyswithmarcella-example.com
Website: www.JourneysWithMarcella-example.com
Social Media Handles for FB,IG, Twitter: JourneysWithMarcella
Colors
Designer to choose colors to be used in the design.
Look and feel

```html
<!DOCTYPE html>
<html lang="en">
<head>
<meta charset="utf-8">
<title>Journeys With Marcella – Business Cards</title>
<link rel="stylesheet" href="https://fonts.googleapis.com/css2?family=Arimo:wght@400;700&display=swap">
<style>
  :root {
    --stage: #8b4d20;
    --card-white: #ffffff;
    --brand-orange: #f5a95a;
    --name-orange: #f3a04a;
    --ink: #1a1a1a;
    --divider: #e3e3e3;
    --shadow: rgba(0, 0, 0, 0.45);
  }
  * { margin: 0; padding: 0; box-sizing: border-box; }
  html, body {
    width: 1200px; height: 900px; overflow: hidden;
    background: var(--stage);
    font-family: "Arimo", Arial, sans-serif;
  }
  .canvas { position: relative; width: 1200px; height: 900px; }

  .card {
    position: absolute;
    border-radius: 14px;
    box-shadow: 3px 4px 6px var(--shadow);
  }
  .card--front { left: 332px; top: 91px; width: 550px; height: 341px; background: var(--card-white); }
  .card--back  { left: 332px; top: 470px; width: 553px; height: 342px; background: var(--brand-orange); }

  .brand {
    position: absolute;
    display: flex; align-items: center; gap: 9px;
    font-weight: 700; white-space: nowrap;
  }
  .brand__mark { display: block; }
  .card--front .brand { left: 20px; top: 160px; font-size: 16px; color: var(--brand-orange); }
  .card--front .brand__mark { width: 14px; height: 14px; background: var(--brand-orange); }
  .card--back .brand { left: 50%; top: 50%; transform: translate(-50%, -50%); font-size: 26px; color: var(--card-white); }
  .card--back .brand__mark { width: 22px; height: 22px; background: var(--card-white); }

  .divider {
    position: absolute; left: 231px; top: 88px;
    width: 1px; height: 164px; background: var(--divider);
  }

  .contact { position: absolute; left: 246px; top: 90px; color: var(--ink); }
  .contact__name {
    font-size: 20px; font-weight: 700; color: var(--name-orange);
    letter-spacing: 0.2px; text-transform: uppercase; line-height: 24px;
  }
  .contact__title { font-size: 15px; line-height: 18px; margin-bottom: 11px; }
  .contact__list { list-style: none; }
  .contact__item {
    display: flex; align-items: center; gap: 5px;
    font-size: 15px; line-height: 21px; white-space: nowrap;
  }
  .contact__item--small { font-size: 12px; letter-spacing: -0.1px; }
  .contact__icon { width: 13px; height: 13px; flex: none; }
  .contact__social {
    display: flex; align-items: center; gap: 7px;
    margin-top: 13px; font-size: 15px; white-space: nowrap;
  }
  .contact__social-dot {
    width: 22px; height: 22px; border-radius: 50%; background: var(--brand-orange);
  }
</style>
</head>
<body>
<main class="canvas">
  <section class="card card--front" aria-label="Business card front">
    <div class="brand">
      <span class="brand__mark"></span>
      <span class="brand__name">Journeys With Marcella</span>
    </div>
    <div class="divider"></div>
    <div class="contact">
      <h1 class="contact__name">Marcella Dorn</h1>
      <p class="contact__title">Travel Designer / Owner</p>
      <ul class="contact__list">
        <li class="contact__item">
          <svg class="contact__icon" viewBox="0 0 16 16" aria-hidden="true">
            <path d="M2 6 C2 3 14 3 14 6 L11 7 L10 5.5 H6 L5 7 Z M4 8 H12 L13 13 H3 Z" fill="var(--brand-orange)"/>
          </svg>
          415-927-3308
        </li>
        <li class="contact__item contact__item--small">
          <svg class="contact__icon" viewBox="0 0 16 16" aria-hidden="true">
            <rect x="1" y="3" width="14" height="10" fill="var(--brand-orange)"/>
            <path d="M1.5 3.5 L8 9 L14.5 3.5" stroke="#fff" stroke-width="1.3" fill="none"/>
          </svg>
          marcella@journeyswithmarcella-example.com
        </li>
        <li class="contact__item contact__item--small">
          <svg class="contact__icon" viewBox="0 0 16 16" aria-hidden="true">
            <circle cx="8" cy="8" r="7" fill="var(--brand-orange)"/>
            <path d="M1 8 H15 M8 1 C5 4 5 12 8 15 M8 1 C11 4 11 12 8 15" stroke="#fff" stroke-width="1" fill="none"/>
          </svg>
          www.JourneysWithMarcella-example.com
        </li>
      </ul>
      <p class="contact__social">
        <span class="contact__social-dot"></span>
        JourneysWithMarcella
      </p>
    </div>
  </section>

  <section class="card card--back" aria-label="Business card back">
    <div class="brand">
      <span class="brand__mark"></span>
      <span class="brand__name">Journeys With Marcella</span>
    </div>
  </section>
</main>
</body>
</html>
```